BAKF Donor Grab brochure design needed

Bright Anchor Kinship Foundation (BAKF) needs brochure (or other marketing piece) that will compel those who see it to read it and activate them donate and support the organization and the Veterans and families it serves. The Bright Anchor Kinship Foundation is a non-profit 501c3 charitable entity that exists for the express purpose of addressing systemic inequities regarding access to and excellence in care provided by the Office of Harbor Affairs, Pioneer’s Care Directorate of Civilian Healthcare Facilities to Veterans and their families. Here is the URL link to the website where txt can be found: www.mybakf.org

Target Market(s)

all ethnicities, patriots, corporate America, other charitable organizations, individual and group donors

Industry/Entity Type

Health and wellness

Other font styles liked:
• Ariel

Requirements
Must have
• excitement, must be compelling, tell a story

```html
<!DOCTYPE html>
<html lang="en">
<head>
<meta charset="utf-8">
<title>BAKF Donor Brochure</title>
<link rel="stylesheet" href="https://fonts.googleapis.com/css2?family=Montserrat:wght@400;600;800&family=Playfair+Display:wght@700&display=swap">
<style>
  :root {
    --green: #1e8a4a;
    --green-dark: #17703b;
    --teal: #1a9c9d;
    --navy: #1f2f4a;
    --ink: #3b4450;
    --muted: #7b838c;
    --paper: #ffffff;
    --stage: #e6e7e9;
    --arc: #d4d7db;
  }
  * { box-sizing: border-box; margin: 0; padding: 0; }
  html, body { width: 839px; height: 1200px; overflow: hidden; }
  body { background: var(--stage); font-family: "Montserrat", Arial, sans-serif; color: var(--ink); position: relative; }
  .spread { position: absolute; left: 30px; width: 780px; height: 540px; display: flex; box-shadow: 0 6px 18px rgba(0,0,0,.18); }
  .spread--outside { top: 40px; }
  .spread--inside { top: 620px; }
  .page { position: relative; width: 390px; height: 540px; background: var(--paper); overflow: hidden; }
  .page + .page { border-left: 1px solid #e2e4e6; }
  .page-art { position: absolute; inset: 0; width: 100%; height: 100%; }
  .txt { position: absolute; }

  /* back cover */
  .about { left: 34px; top: 268px; width: 320px; font-size: 10.5px; line-height: 1.6; color: var(--ink); }
  .contact-title { left: 34px; top: 360px; font-size: 13px; font-weight: 800; color: var(--green); letter-spacing: .5px; }
  .contact-list { left: 34px; top: 386px; list-style: none; font-size: 10.5px; line-height: 1.9; color: var(--ink); }
  .contact-list li { display: flex; align-items: center; gap: 8px; }
  .contact-list svg { width: 12px; height: 12px; fill: var(--green); }
  .social { right: 40px; top: 392px; display: flex; gap: 6px; }
  .social span { width: 18px; height: 18px; border-radius: 50%; background: var(--green); display: block; }

  /* front cover */
  .brand { left: 150px; top: 28px; display: flex; align-items: center; gap: 8px; }
  .brand-dot { width: 26px; height: 26px; border-radius: 50%; background: var(--green); }
  .brand-name { font-size: 17px; font-weight: 800; color: var(--green); letter-spacing: 1px; }
  .headline { left: 38px; top: 268px; width: 170px; text-align: center; font-size: 15px; font-weight: 800; line-height: 1.2; color: #fff; text-transform: uppercase; }
  .headline small { display: block; font-weight: 400; font-size: 14px; }
  .web { right: 34px; bottom: 34px; font-size: 12px; font-weight: 600; color: var(--navy); letter-spacing: .5px; }

  /* pillars */
  .pillars-title { left: 40px; top: 34px; font-family: "Playfair Display", Georgia, serif; color: var(--navy); font-size: 26px; line-height: 1.1; }
  .pillars-title em { display: block; font-style: normal; color: var(--teal); }
  .pillar-list { left: 40px; top: 118px; list-style: none; width: 310px; }
  .pillar-list li { display: flex; align-items: center; gap: 10px; margin-bottom: 7px; font-size: 10.5px; color: var(--ink); }
  .pillar-num { width: 64px; height: 22px; background: var(--green); color: #fff; font-weight: 800; font-size: 11px; display: flex; align-items: center; justify-content: center; }

  /* impact */
  .impact-title { left: 34px; top: 226px; font-size: 16px; font-weight: 800; color: var(--green); letter-spacing: .5px; }
  .impact-list { left: 34px; top: 258px; list-style: none; width: 330px; }
  .impact-list li { display: flex; align-items: center; gap: 12px; margin-bottom: 14px; }
  .impact-icon { flex: none; width: 44px; height: 44px; border-radius: 50%; background: linear-gradient(135deg, #9fb5c4, #5f7d92); border: 2px solid var(--teal); }
  .impact-list h3 { font-size: 11px; font-weight: 800; color: var(--navy); }
  .impact-list p { font-size: 10px; color: var(--muted); line-height: 1.4; }
</style>
</head>
<body>

<section class="spread spread--outside">
  <article class="page page--back">
    <svg class="page-art" viewBox="0 0 390 540">
      <defs>
        <linearGradient id="groupTone" x1="0" y1="0" x2="1" y2="1">
          <stop offset="0" stop-color="#c9b8a6"/><stop offset="1" stop-color="#6f7f8e"/>
        </linearGradient>
      </defs>
      <path d="M0 0H390V200Q300 250 190 230Q80 212 0 240Z" fill="url(#groupTone)" role="img" aria-label="Photo of veterans and family members standing together"/>
      <circle cx="330" cy="220" r="34" fill="var(--teal)"/>
      <circle cx="282" cy="244" r="14" fill="var(--green)"/>
      <path d="M240 540A170 170 0 0 1 390 380V540Z" fill="var(--arc)" opacity=".5"/>
    </svg>
    <p class="txt about">Bright Anchor Kinship Foundation works to close gaps in access to quality care for veterans and their families, linking them with trusted civilian providers and lasting community support.</p>
    <h2 class="txt contact-title">GET IN TOUCH WITH US:</h2>
    <ul class="txt contact-list">
      <li><svg viewBox="0 0 24 24"><path d="M6.6 10.8a15 15 0 0 0 6.6 6.6l2.2-2.2c.3-.3.7-.4 1-.2 1.1.4 2.3.6 3.6.6.6 0 1 .4 1 1V20c0 .6-.4 1-1 1C10.6 21 3 13.4 3 4c0-.6.4-1 1-1h3.5c.6 0 1 .4 1 1 0 1.3.2 2.5.6 3.6.1.3 0 .7-.2 1z"/></svg>(555) 014-2290</li>
      <li><svg viewBox="0 0 24 24"><path d="M12 2a7 7 0 0 0-7 7c0 5 7 13 7 13s7-8 7-13a7 7 0 0 0-7-7zm0 9.5A2.5 2.5 0 1 1 12 6.5a2.5 2.5 0 0 1 0 5z"/></svg>12 Harborview Lane, Suite 4, Bayport</li>
      <li><svg viewBox="0 0 24 24"><path d="M3 5h18v14H3zm2 2v.5l7 4.5 7-4.5V7z"/></svg>info@mybakf.org</li>
    </ul>
    <div class="txt social"><span></span><span></span></div>
  </article>

  <article class="page page--front">
    <svg class="page-art" viewBox="0 0 390 540">
      <defs>
        <linearGradient id="familyTone" x1="0" y1="0" x2="1" y2="1">
          <stop offset="0" stop-color="#d9c3ae"/><stop offset="1" stop-color="#7e8f9c"/>
        </linearGradient>
      </defs>
      <path d="M250 540A200 200 0 0 1 390 320V540Z" fill="var(--arc)" opacity=".6"/>
      <circle cx="230" cy="250" r="156" fill="var(--teal)" opacity=".25"/>
      <circle cx="230" cy="250" r="148" fill="url(#familyTone)" role="img" aria-label="Photo of a veteran family smiling together"/>
      <circle cx="122" cy="300" r="92" fill="var(--green)"/>
      <circle cx="330" cy="400" r="20" fill="var(--teal)"/>
    </svg>
    <div class="txt brand"><span class="brand-dot"></span><span class="brand-name">BRIGHT ANCHOR</span></div>
    <h1 class="txt headline">Caring for veterans and their families <small>who have borne the battle</small></h1>
    <p class="txt web">www.mybakf.org</p>
  </article>
</section>

<section class="spread spread--inside">
  <article class="page page--pillars">
    <svg class="page-art" viewBox="0 0 390 540">
      <defs>
        <linearGradient id="studentTone" x1="0" y1="0" x2="1" y2="1">
          <stop offset="0" stop-color="#c7a98c"/><stop offset="1" stop-color="#6c6a5e"/>
        </linearGradient>
        <linearGradient id="classTone" x1="0" y1="0" x2="1" y2="1">
          <stop offset="0" stop-color="#8d9aa6"/><stop offset="1" stop-color="#4b5866"/>
        </linearGradient>
      </defs>
      <circle cx="110" cy="450" r="120" fill="url(#studentTone)" role="img" aria-label="Photo of a smiling student holding books"/>
      <rect x="230" y="370" width="160" height="140" fill="url(#classTone)" role="img" aria-label="Photo of a classroom lecture"/>
      <circle cx="232" cy="360" r="26" fill="var(--teal)"/>
      <circle cx="360" cy="330" r="12" fill="var(--green)"/>
    </svg>
    <h2 class="txt pillars-title">Five Strategic Pillars <em>for Success</em></h2>
    <ol class="txt pillar-list">
      <li><span class="pillar-num">01</span>Expand access to care</li>
      <li><span class="pillar-num">02</span>Strengthen family support</li>
      <li><span class="pillar-num">03</span>Build community partnerships</li>
      <li><span class="pillar-num">04</span>Advance health equity</li>
      <li><span class="pillar-num">05</span>Grow lasting donor trust</li>
    </ol>
  </article>

  <article class="page page--impact">
    <svg class="page-art" viewBox="0 0 390 540">
      <defs>
        <linearGradient id="careTone" x1="0" y1="0" x2="1" y2="1">
          <stop offset="0" stop-color="#b9d3dc"/><stop offset="1" stop-color="#4f7890"/>
        </linearGradient>
      </defs>
      <path d="M0 0H390V170Q290 215 170 200Q70 188 0 205Z" fill="url(#careTone)" role="img" aria-label="Photo of medical staff caring for a patient"/>
      <circle cx="40" cy="200" r="22" fill="var(--teal)"/>
      <path d="M270 540A150 150 0 0 1 390 400V540Z" fill="var(--arc)" opacity=".5"/>
    </svg>
    <h2 class="txt impact-title">OUR IMPACT AREAS</h2>
    <ul class="txt impact-list">
      <li><span class="impact-icon" role="img" aria-label="Photo of a veteran at a clinic"></span><div><h3>Care Access</h3><p>Connecting veterans with trusted local clinics.</p></div></li>
      <li><span class="impact-icon" role="img" aria-label="Photo of a family at home"></span><div><h3>Family Wellness</h3><p>Support services for spouses and children at home.</p></div></li>
      <li><span class="impact-icon" role="img" aria-label="Photo of a counseling session"></span><div><h3>Mental Health</h3><p>Counseling and peer groups for healing after service.</p></div></li>
      <li><span class="impact-icon" role="img" aria-label="Photo of a hospital hallway"></span><div><h3>Quality Advocacy</h3><p>Pushing for equal standards across civilian care.</p></div></li>
    </ul>
  </article>
</section>

</body>
</html>
```